Harborline Network Advisors (HNA) Business Card

Front Side, add Company Logo
1.) Harborline Network Advisors
Director of Operations
Delgado, Marco T
(323) 555 0148
782 n Alder Ave Suite 300 PMB2093
Los Angeles, CA 90013
Marco@HarborlineNA.example
www.HarborlineNA.example
2.) Veteran-Owned Business (with Small EGA)

Back Side
- Pictures are ideas of what you can add. The description is what HNA does.
1.) Business Partners:
- Corvalis Business
- KX&L Business
- Tellmora Business
2.) What we do
- Broker of Internet service (partners above)
- Project Management/ Contract Management
- Government Contracts

```html
<!DOCTYPE html>
<html lang="en">
<head>
<meta charset="utf-8">
<title>Harborline Network Advisors – Business Card</title>
<link rel="stylesheet" href="https://fonts.googleapis.com/css2?family=Quicksand:wght@400;500;600;700&display=swap">
<style>
  :root {
    --page: #d8d3cc;
    --card: #1d1b1a;
    --gold: #f2b01e;
    --ink: #ebe8e4;
    --tile: #f7f7f5;
    --tile-ink: #1f2a4a;
    --faint: #2a2622;
  }
  * { box-sizing: border-box; margin: 0; padding: 0; }
  html, body {
    width: 1200px; height: 900px; overflow: hidden;
    background: var(--page);
    font-family: "Quicksand", sans-serif;
  }
  .sheet {
    width: 1200px; height: 900px;
    display: flex; flex-direction: column; align-items: center; justify-content: center;
    gap: 44px;
  }
  .card {
    position: relative;
    width: 700px; height: 400px;
    background: var(--card);
    border-radius: 34px;
    color: var(--ink);
    overflow: hidden;
    box-shadow: 0 14px 30px rgba(0,0,0,.25);
  }

  /* brand mark: name set in text beside a plain circle */
  .brand {
    position: absolute;
    display: flex; flex-direction: column; align-items: center; justify-content: center;
    width: 170px; height: 170px;
    border: 2px solid var(--gold);
    border-radius: 50%;
    text-align: center;
    color: var(--gold);
    font-weight: 700;
  }
  .brand-initials { font-size: 46px; letter-spacing: 2px; line-height: 1; }
  .brand-name { font-size: 11px; letter-spacing: 1.5px; text-transform: uppercase; margin-top: 8px; line-height: 1.4; padding: 0 18px; }

  /* back side */
  .back .brand { top: 34px; right: 46px; }
  .section-label { color: var(--gold); font-weight: 600; font-size: 19px; }
  .partners { position: absolute; left: 50px; top: 150px; }
  .partner-row { display: flex; gap: 12px; margin-top: 12px; }
  .partner-tile {
    width: 150px; height: 52px;
    background: var(--tile);
    display: flex; align-items: center; justify-content: center;
    color: var(--tile-ink); font-weight: 700; font-size: 15px;
  }
  .services { position: absolute; left: 50px; top: 262px; }
  .service-list { list-style: none; margin-top: 6px; }
  .service-list li {
    display: flex; align-items: center; gap: 10px;
    font-size: 17px; font-weight: 500; line-height: 1.55;
  }
  .bullet { width: 16px; height: 14px; flex: none; }

  /* front side */
  .front .brand { left: 50px; top: 50px; width: 200px; height: 200px; }
  .front .brand-initials { font-size: 56px; }
  .watermark {
    position: absolute; right: 40px; top: 20px; z-index: 0;
    font-size: 150px; font-weight: 700; color: var(--faint);
    letter-spacing: 4px; line-height: 1;
  }
  .person {
    position: absolute; right: 318px; top: 290px;
    text-align: right; white-space: nowrap;
  }
  .person-name { color: var(--gold); font-size: 24px; font-weight: 600; }
  .person-title { font-size: 17px; font-weight: 500; margin-top: 2px; }
  .divider {
    position: absolute; left: 400px; top: 205px;
    width: 1px; height: 165px; background: var(--ink); opacity: .7;
  }
  .contact {
    position: absolute; left: 418px; top: 218px;
    list-style: none; font-size: 13px; font-weight: 500; line-height: 1.5;
    white-space: nowrap;
  }
  .contact li { display: flex; gap: 8px; align-items: flex-start; margin-bottom: 4px; }
  .contact svg { width: 14px; height: 14px; flex: none; margin-top: 3px; fill: var(--gold); }
</style>
</head>
<body>
<main class="sheet">

  <section class="card back" aria-label="Card back">
    <div class="brand" aria-label="Harborline Network Advisors">
      <span class="brand-initials">HNA</span>
      <span class="brand-name">Harborline Network Advisors</span>
    </div>

    <div class="partners">
      <p class="section-label">Business Partners -</p>
      <div class="partner-row">
        <div class="partner-tile">KX&amp;L Business</div>
        <div class="partner-tile">Corvalis Business</div>
        <div class="partner-tile">Tellmora Business</div>
      </div>
    </div>

    <div class="services">
      <p class="section-label">What we do -</p>
      <ul class="service-list">
        <li><svg class="bullet" viewBox="0 0 16 14"><path d="M0 0 L16 7 L0 14 L5 7 Z" fill="#f2b01e"/></svg>Broker of Internet service (partners above)</li>
        <li><svg class="bullet" viewBox="0 0 16 14"><path d="M0 0 L16 7 L0 14 L5 7 Z" fill="#f2b01e"/></svg>Project Management/ Contract Management</li>
        <li><svg class="bullet" viewBox="0 0 16 14"><path d="M0 0 L16 7 L0 14 L5 7 Z" fill="#f2b01e"/></svg>Government Contracts</li>
      </ul>
    </div>
  </section>

  <section class="card front" aria-label="Card front">
    <span class="watermark" aria-hidden="true">HNA</span>

    <div class="brand" aria-label="Harborline Network Advisors">
      <span class="brand-initials">HNA</span>
      <span class="brand-name">Harborline Network Advisors</span>
    </div>

    <div class="person">
      <p class="person-name">Delgado, Marco T</p>
      <p class="person-title">Director of Operations</p>
    </div>

    <div class="divider"></div>

    <ul class="contact">
      <li><svg viewBox="0 0 24 24"><path d="M3 8c0-2 4-4 9-4s9 2 9 4v2h-5V8H8v2H3z M6 12h12l2 8H4z"/></svg>(323) 555 0148</li>
      <li><svg viewBox="0 0 24 24"><path d="M2 6h20v12H2z M2 6l10 7 10-7" stroke="#1d1b1a" stroke-width="1.5"/></svg>Marco@HarborlineNA.example</li>
      <li><svg viewBox="0 0 24 24"><circle cx="12" cy="12" r="10"/><path d="M2 12h20 M12 2c4 4 4 16 0 20 M12 2c-4 4-4 16 0 20" stroke="#1d1b1a" stroke-width="1.5" fill="none"/></svg>www.HarborlineNA.example</li>
      <li><svg viewBox="0 0 24 24"><path d="M12 2a7 7 0 0 0-7 7c0 5 7 13 7 13s7-8 7-13a7 7 0 0 0-7-7z"/><circle cx="12" cy="9" r="2.6" fill="#1d1b1a"/></svg><span>782 n Alder Ave Suite 300 PMB2093<br>Los Angeles, CA 90013</span></li>
    </ul>
  </section>

</main>
</body>
</html>
```